Moden - Mexicali - Flower Shop

brisapetals is looking for a cool web design that has a airy, clean, mexicali feel to it.

See attached images and links for idea of what we mean with the above.

please no templates.

Target Market(s)

Local flower shop in San Diego, California

Industry/Entity Type

Shop

Requirements
Must have
• see. brisapetals.quartzcart.example - I did the site and logo...I love the logo - hate the site.

Going for this feel: http://www.velmorastudio.example/platebook/archives/tovarinos.php

I also attached another site I liked- I just feel like it may be to busy.

```html
<!DOCTYPE html>
<html lang="en">
<head>
<meta charset="utf-8">
<title>Brisa Petals — Online Flower Shop</title>
<link rel="stylesheet" href="https://fonts.googleapis.com/css2?family=Oxygen:wght@300;400;700&display=swap">
<style>
:root{
  --ink:#2b2b2b;
  --text:#555;
  --muted:#8a8a8a;
  --rule:#d9d9d9;
  --accent:#4aa88f;
  --logo:#5fb3a2;
  --footer:#3b3b39;
  --footer-deep:#2e2e2c;
  --white:#fff;
  --button:#2ea6dd;
}
*{box-sizing:border-box;margin:0;padding:0}
html,body{width:1200px;height:2237px;overflow:hidden}
body{background:var(--white);font-family:"Oxygen",Arial,sans-serif;color:var(--ink);position:relative}
.wrap{position:absolute;left:85px;width:1030px}

.top-bar{top:0;height:56px;border-top:2px solid var(--ink);border-bottom:1px solid #e6e6e6;display:flex;align-items:center;justify-content:space-between;font-size:14px;color:var(--text)}
.account-links span{margin:0 7px;color:#999}
.tools{display:flex;align-items:center;gap:70px}
.search{width:262px;height:32px;border:1px solid #e3e3e3;display:flex;align-items:center;justify-content:space-between;padding:0 12px;color:#888;font-size:14px}
.cart{display:flex;align-items:center;gap:12px;font-size:14px}

.brand{top:88px;text-align:center;font-size:46px;letter-spacing:16px;color:var(--logo);font-weight:400;line-height:60px}

.main-nav{top:180px;height:59px;border-top:2px solid var(--ink);border-bottom:2px solid var(--ink);display:flex;align-items:center;font-size:18px;color:#444;white-space:nowrap}
.main-nav a{color:inherit;text-decoration:none;text-align:center;border-left:1px solid var(--rule);line-height:26px;display:flex;align-items:center;justify-content:center}
.main-nav .home{border-left:none;width:126px}
.main-nav .shop{width:143px}
.main-nav .fresh{width:214px}
.main-nav .curated{width:262px}
.main-nav .blog{width:107px}
.main-nav .contact{width:178px}

.hero{top:265px;height:484px;background:radial-gradient(ellipse at 48% 42%,#f2f2ee 0%,#dcdcd4 28%,#7d8a5a 52%,#9a9a92 75%,#bfc6c6 100%)}
.hero-arrow{position:absolute;top:220px;width:42px;height:76px;background:var(--white);display:flex;align-items:center;justify-content:center}
.hero-arrow.left{left:0;clip-path:polygon(0 0,100% 50%,0 100%)}
.hero-arrow.right{right:0;clip-path:polygon(100% 0,0 50%,100% 100%)}
.hero-arrow svg{position:absolute}
.hero-arrow.left svg{left:2px}
.hero-arrow.right svg{right:2px}

.welcome{top:820px;display:flex;gap:48px}
.welcome h1{width:290px;flex:none;text-align:right;font-weight:300;font-size:29px;line-height:42px;color:#555;text-transform:uppercase;white-space:nowrap;direction:rtl}
.welcome h1 span{direction:ltr;unicode-bidi:isolate}
.welcome h1 em{font-style:normal;color:var(--accent)}
.welcome p{flex:1;font-size:13.5px;line-height:26px;color:var(--text);padding-top:5px}

.tabs{top:964px;display:flex;align-items:center;gap:16px;font-size:17px;letter-spacing:2px}
.tabs .line{flex:1;height:2px;background:var(--ink)}
.tabs .dot{width:8px;height:8px;border-radius:50%;background:var(--ink)}
.tabs .active{color:#333}
.tabs .idle{color:var(--muted)}

.pager{top:1017px;left:537px;width:130px;display:flex;gap:6px}
.pager span{height:27px;width:62px;background:#111;color:var(--white);font-size:12px;display:flex;align-items:center;justify-content:center}
.pager .prev{clip-path:polygon(14% 0,100% 0,100% 100%,14% 100%,0 50%)}
.pager .next{clip-path:polygon(0 0,86% 0,100% 50%,86% 100%,0 100%)}

.product-grid{top:1093px;display:grid;grid-template-columns:repeat(4,225px);column-gap:43px;row-gap:50px}
.product{height:311px;border:1px solid var(--rule);text-align:center;padding-top:16px}
.product .photo{width:186px;height:172px;margin:0 auto}
.product h3{font-weight:400;font-size:16px;color:#333;margin-top:18px;white-space:nowrap}
.product .price{font-family:Arial,sans-serif;font-size:18px;color:#222;margin-top:18px}
.product .stars{margin-top:8px}

.tone-1{background:radial-gradient(circle at 50% 45%,#e35f93 0%,#f3d7e1 45%,#f7f7f7 75%)}
.tone-2{background:radial-gradient(circle at 50% 40%,#f0c52a 0%,#e78a2d 30%,#c9d58e 55%,#f7f7f7 78%)}
.tone-3{background:radial-gradient(circle at 50% 45%,#d7255f 0%,#f08cb0 40%,#f7f7f7 75%)}
.tone-4{background:radial-gradient(circle at 50% 40%,#f4d21f 0%,#6a3d9a 40%,#b9c98a 58%,#f7f7f7 78%)}
.tone-5{background:radial-gradient(circle at 50% 45%,#9d4ab0 0%,#9fc83a 45%,#f7f7f7 76%)}
.tone-6{background:radial-gradient(circle at 50% 42%,#f4a6c4 0%,#b385d0 40%,#f7f7f7 76%)}
.tone-7{background:radial-gradient(circle at 50% 40%,#ee6a2a 0%,#f4b63b 35%,#7aa04a 55%,#f7f7f7 78%)}
.tone-8{background:radial-gradient(circle at 50% 42%,#f5d128 0%,#ee5a8c 40%,#f7f7f7 76%)}

.site-footer{position:absolute;left:0;top:1838px;width:1200px;height:399px;background:radial-gradient(ellipse at 30% 30%,#4a4a47 0%,var(--footer) 45%,var(--footer-deep) 100%);color:var(--white)}
.footer-col{position:absolute;top:56px}
.footer-col h2{font-weight:400;font-size:26px;margin-bottom:22px}
.footer-col p{font-size:13.5px;line-height:27px}
.meet{left:85px;width:300px}
.socials{display:flex;gap:15px;margin-top:14px}
.socials span{width:42px;height:42px;border-radius:50%;background:var(--white)}
.reach{left:514px}
.contact-row{display:flex;gap:18px;font-size:13.5px;line-height:27px;margin-bottom:16px}
.contact-row svg{flex:none;margin-top:4px}
.news{left:826px;width:290px}
.signup{display:flex;margin-top:26px}
.signup .field{width:198px;height:40px;background:linear-gradient(#e4e4e4,#f6f6f6)}
.signup .submit{width:88px;height:40px;background:var(--button);font-weight:700;font-size:17px;display:flex;align-items:center;justify-content:center}
.footer-rule{position:absolute;left:85px;top:304px;width:1030px;height:1px;background:#5e5e5b}
.footer-bottom{position:absolute;left:90px;top:343px;width:1022px;display:flex;justify-content:space-between;font-size:14px}
</style>
</head>
<body>

<header class="wrap top-bar">
  <div class="account-links">Register<span>|</span>Login<span>|</span>My Account</div>
  <div class="tools">
    <div class="search">Search
      <svg width="14" height="14" viewBox="0 0 14 14"><circle cx="6" cy="6" r="4.5" fill="none" stroke="#999" stroke-width="2"/><line x1="9.3" y1="9.3" x2="13" y2="13" stroke="#999" stroke-width="2"/></svg>
    </div>
    <div class="cart">
      <svg width="24" height="20" viewBox="0 0 24 20"><path d="M1 2h4l3 11h12l3-8H7" fill="none" stroke="#333" stroke-width="2"/><circle cx="9" cy="17" r="2" fill="#333"/><circle cx="19" cy="17" r="2" fill="#333"/></svg>
      Items (0)
    </div>
  </div>
</header>

<div class="wrap brand">BRISA PETALS</div>

<nav class="wrap main-nav">
  <a class="home" href="#" aria-label="Home">
    <svg width="32" height="28" viewBox="0 0 32 28"><path d="M16 2 1 15h5v12h8v-8h4v8h8V15h5z" fill="#222"/></svg>
  </a>
  <a class="shop" href="#">OUR SHOP</a>
  <a class="fresh" href="#">FRESH THIS WEEK</a>
  <a class="curated" href="#">CURATED COLLECTIONS</a>
  <a class="blog" href="#">BLOG</a>
  <a class="contact" href="#">CONTACT US</a>
</nav>

<section class="wrap hero" role="img" aria-label="Photo of a white tulip and lily bouquet with pearl accents resting on stone beside a waterfront">
  <div class="hero-arrow left"><svg width="14" height="24" viewBox="0 0 14 24"><path d="M11 2 2 12l9 10" fill="none" stroke="#333" stroke-width="1.5"/></svg></div>
  <div class="hero-arrow right"><svg width="14" height="24" viewBox="0 0 14 24"><path d="M3 2l9 10-9 10" fill="none" stroke="#333" stroke-width="1.5"/></svg></div>
</section>

<section class="wrap welcome">
  <h1><span>Welcome to</span><br><span>our <em>Online Store</em></span></h1>
  <p>Duis autem vel eum iriure dolor in hendrerit in vulputate velit esse molestie consequat, vel illum dolore eu feugiat nulla facilisis at vero eros et accumsan et iusto. Nam liber tempor cum soluta nobis eleifend option congue nihil imperdiet doming. Nam liber tempor cum soluta nobis eleifend option congue nihil imperdiet.</p>
</section>

<div class="wrap tabs">
  <span class="line"></span><span class="dot"></span>
  <span class="active">FRESH THIS WEEK</span><span class="dot"></span>
  <span class="idle">CURATED COLLECTIONS</span><span class="dot"></span>
  <span class="line"></span>
</div>

<div class="wrap pager"><span class="prev">prev</span><span class="next">next</span></div>

<section class="wrap product-grid">
  <article class="product"><div class="photo tone-1" role="img" aria-label="Pink and white flower bouquet in a polka dot box"></div><h3>Beciegast nveriti vaert</h3><div class="price">$119.50</div><div class="stars"><svg width="66" height="11" viewBox="0 0 66 11"><g fill="none" stroke="#aaa" stroke-width=".8"><path id="s" d="M5.5 .8l1.4 3 3.2.3-2.4 2.1.7 3.2-2.9-1.7-2.9 1.7.7-3.2L.9 4.1l3.2-.3z"/><use href="#s" x="13"/><use href="#s" x="26"/><use href="#s" x="39"/><use href="#s" x="52"/></g></svg></div></article>
  <article class="product"><div class="photo tone-2" role="img" aria-label="Yellow and orange lily bouquet in a glass vase"></div><h3>Beciegast nveriti vaert</h3><div class="price">$119.50</div><div class="stars"><svg width="66" height="11" viewBox="0 0 66 11"><g fill="none" stroke="#aaa" stroke-width=".8"><use href="#s"/><use href="#s" x="13"/><use href="#s" x="26"/><use href="#s" x="39"/><use href="#s" x="52"/></g></svg></div></article>
  <article class="product"><div class="photo tone-3" role="img" aria-label="Pink lily and rose bouquet in a square vase"></div><h3>Beciegast nveriti vaert</h3><div class="price">$119.50</div><div class="stars"><svg width="66" height="11" viewBox="0 0 66 11"><g fill="none" stroke="#aaa" stroke-width=".8"><use href="#s"/><use href="#s" x="13"/><use href="#s" x="26"/><use href="#s" x="39"/><use href="#s" x="52"/></g></svg></div></article>
  <article class="product"><div class="photo tone-4" role="img" aria-label="Yellow and purple flower bouquet in a clear vase"></div><h3>Beciegast nveriti vaert</h3><div class="price">$119.50</div><div class="stars"><svg width="66" height="11" viewBox="0 0 66 11"><g fill="none" stroke="#aaa" stroke-width=".8"><use href="#s"/><use href="#s" x="13"/><use href="#s" x="26"/><use href="#s" x="39"/><use href="#s" x="52"/></g></svg></div></article>
  <article class="product"><div class="photo tone-5" role="img" aria-label="Purple and green flower bouquet in a violet cube vase"></div><h3>Beciegast nveriti vaert</h3><div class="price">$119.50</div><div class="stars"><svg width="66" height="11" viewBox="0 0 66 11"><g fill="none" stroke="#aaa" stroke-width=".8"><use href="#s"/><use href="#s" x="13"/><use href="#s" x="26"/><use href="#s" x="39"/><use href="#s" x="52"/></g></svg></div></article>
  <article class="product"><div class="photo tone-6" role="img" aria-label="Pastel pink and lavender rose bouquet in a glass vase"></div><h3>Beciegast nveriti vaert</h3><div class="price">$119.50</div><div class="stars"><svg width="66" height="11" viewBox="0 0 66 11"><g fill="none" stroke="#aaa" stroke-width=".8"><use href="#s"/><use href="#s" x="13"/><use href="#s" x="26"/><use href="#s" x="39"/><use href="#s" x="52"/></g></svg></div></article>
  <article class="product"><div class="photo tone-7" role="img" aria-label="Orange and red mixed flower bouquet in a tall vase"></div><h3>Beciegast nveriti vaert</h3><div class="price">$119.50</div><div class="stars"><svg width="66" height="11" viewBox="0 0 66 11"><g fill="none" stroke="#aaa" stroke-width=".8"><use href="#s"/><use href="#s" x="13"/><use href="#s" x="26"/><use href="#s" x="39"/><use href="#s" x="52"/></g></svg></div></article>
  <article class="product"><div class="photo tone-8" role="img" aria-label="Yellow lily and pink flower bouquet in a pink vase"></div><h3>Beciegast nveriti vaert</h3><div class="price">$119.50</div><div class="stars"><svg width="66" height="11" viewBox="0 0 66 11"><g fill="none" stroke="#aaa" stroke-width=".8"><use href="#s"/><use href="#s" x="13"/><use href="#s" x="26"/><use href="#s" x="39"/><use href="#s" x="52"/></g></svg></div></article>
</section>

<footer class="site-footer">
  <div class="footer-col meet">
    <h2>Meet Brisa</h2>
    <p>Based in Hillcrest, San Diego - We offer farm fresh, curated, cool, and same day delivery flower bouquets. miuagtarsa nerafae kertyerauas.</p>
    <div class="socials"><span></span><span></span><span></span></div>
  </div>
  <div class="footer-col reach">
    <h2>Reach Brisa</h2>
    <div class="contact-row"><svg width="16" height="22" viewBox="0 0 16 22"><path d="M8 0a8 8 0 0 0-8 8c0 6 8 14 8 14s8-8 8-14a8 8 0 0 0-8-8zm0 11a3 3 0 1 1 0-6 3 3 0 0 1 0 6z" fill="#fff"/></svg><span>2280 Canyon Vista Avenue<br>San Diego, CA 92103</span></div>
    <div class="contact-row"><svg width="24" height="16" viewBox="0 0 24 16"><rect width="24" height="16" fill="#fff"/><path d="M1 1l11 8 11-8" fill="none" stroke="#3b3b39" stroke-width="1.5"/></svg><span>info@brisapetals.example</span></div>
    <div class="contact-row"><svg width="20" height="20" viewBox="0 0 20 20"><path d="M4 1l4 4-2 3c1 3 3 5 6 6l3-2 4 4-3 3C8 19 1 12 1 4z" fill="#fff"/></svg><span>619-555-0142</span></div>
  </div>
  <div class="footer-col news">
    <h2>Newsletter</h2>
    <p>We promise to only send you good things like discounts!</p>
    <div class="signup"><div class="field"></div><div class="submit">SUBMIT</div></div>
  </div>
  <div class="footer-rule"></div>
  <div class="footer-bottom">
    <span>Terms and Conditions | Privacy Policy | Site Map</span>
    <span>Copyright © 2013. All Rights Reserved.</span>
  </div>
</footer>

</body>
</html>
```